Design mobile friendly review and ranking site

We're working on a corporate website for reviewing and ranking fellow employees. We need the website to look both fun and professional and it needs to be responsive - to it works on mobile and desktop.

Looking for css and HTML for 3 key pages as well as a header and footer for the site. Also would need any supporting graphics as part of the design.

Target Market(s)

Professionals in their 20s, 30s, and 40s.

Industry/Entity Type

Internet

Coding

Coded - Design and coding required

Number of Pages Required

3 page

Font styles to use
Sans Serif

Requirements
Must have
• 3 key pages we need (note included screenshots for each - these are just super rough cuts so you see examples of the content.)
• a) main-intro: A compelling into page with a login/registration form. Should be sleek/modern/enticing. Also we would show the ranking for the top 3 people to tease people re: content.
• b) main-page: Has two sections: One at the top where you would rate someone and one at the bottom where it shows a ranking of people.
• c) profile page: This is where you view a specific person. You see the person's picture, some info about the person, you see their overall rating, you can rate them, and you also see their historical ratings.
Nice to have
• Note we need css and HTML for this. It should feel as sleek and modern. Note also must be responsive design so it works well in mobile and desktop.

```html
<!DOCTYPE html>
<html lang="en">
<head>
<meta charset="utf-8">
<title>PeerScore Hub</title>
<link href="https://fonts.googleapis.com/css2?family=Mulish:wght@300;400;600;700&display=swap" rel="stylesheet">
<style>
:root{
  --green:#1a5c44;
  --orange:#f47b08;
  --orange-light:#ff9a0a;
  --text:#333333;
  --band:#efefef;
  --line:#c9c9c9;
  --footer:#3c3c3c;
  --white:#ffffff;
}
*{box-sizing:border-box;margin:0;padding:0}
html,body{width:1200px;height:1053px;overflow:hidden}
body{font-family:"Mulish",sans-serif;color:var(--text);background:var(--white);position:relative}
.site-header{height:96px;position:relative}
.brand{position:absolute;left:76px;top:20px}
.brand-name{font-size:34px;font-weight:600;color:var(--green);line-height:1.1;letter-spacing:-.3px}
.brand-tag{font-size:14.5px;margin-top:2px}
.user-bar{position:absolute;right:74px;top:40px;font-size:14.5px;display:flex;align-items:center;gap:8px;color:#666}
.level{color:var(--orange);margin-right:20px}
.user-bar svg{width:13px;height:13px;fill:#666}
.auth-band{background:var(--band);height:515px;position:relative}
.auth-card{position:absolute;left:247px;top:72px;width:705px;height:399px;background:var(--white);text-align:center}
.section-title{font-size:32px;font-weight:300;color:#222;letter-spacing:.3px}
.auth-card .section-title{margin-top:32px}
.divider{width:90px;height:2px;background:#ccc;margin:20px auto 0}
.form-grid{position:absolute;left:21px;top:118px;display:grid;grid-template-columns:323px 323px;column-gap:18px;row-gap:18px}
.field{height:38px;border:1px solid var(--line);font-size:13.5px;color:#555;text-align:left;padding:0 15px;display:flex;align-items:center}
.submit{position:absolute;left:191px;top:289px;width:323px;height:42px;border-radius:21px;background:linear-gradient(var(--orange-light),var(--orange));box-shadow:0 0 0 3px #e4e4e4;color:#fff;font-weight:700;font-size:15px;display:flex;align-items:center;justify-content:center}
.login-link{position:absolute;left:0;right:0;top:348px;font-size:15px;font-weight:700;color:var(--green);text-decoration:underline}
.rankings{text-align:center;padding-top:40px;height:367px;position:relative}
.rank-card{position:absolute;top:133px;width:320px;text-align:left}
.avatar{position:absolute;left:0;top:0;width:62px;height:62px;border-radius:50%;background:radial-gradient(circle at 50% 40%,#d9c2b0,#8a7a70)}
.avatar.dark{background:radial-gradient(circle at 50% 40%,#cdb5a2,#222)}
.rank-body{position:absolute;left:75px;top:0;width:242px}
.rank-no{font-size:15px;font-weight:700;color:#333;line-height:1}
.rank-name{font-size:22px;font-weight:700;color:var(--green);margin-top:7px;line-height:1}
.rank-points{font-size:15px;color:var(--orange);margin-top:6px}
.rank-reviews{font-size:14.5px;margin-top:7px}
.rank-reviews span{color:var(--green)}
.trait{display:flex;justify-content:space-between;align-items:center;font-size:13.5px;margin-top:12px}
.trait + .trait{margin-top:14px}
.stars{display:flex;gap:2px}
.stars svg{width:14px;height:14px}
.site-footer{position:absolute;left:0;top:978px;width:1200px;height:75px;background:var(--footer);color:#bbb;font-size:13.5px;text-align:center;padding-top:31px}
</style>
</head>
<body>
<svg width="0" height="0" style="position:absolute">
  <symbol id="star-full" viewBox="0 0 24 24"><path d="M12 2l3 7 7.5.6-5.7 5 1.8 7.4L12 18l-6.6 4 1.8-7.4-5.7-5L9 9z" fill="#f47b08"/></symbol>
  <symbol id="star-empty" viewBox="0 0 24 24"><path d="M12 3.5l2.6 6 6.4.5-4.9 4.3 1.5 6.3L12 17.2l-5.6 3.4 1.5-6.3L3 10l6.4-.5z" fill="none" stroke="#f47b08" stroke-width="1.8"/></symbol>
</svg>

<header class="site-header">
  <div class="brand">
    <div class="brand-name">PeerScore Hub</div>
    <div class="brand-tag">Share this to get more points</div>
  </div>
  <nav class="user-bar">
    <span class="level">Level 3 41 points to Level 4</span>
    <svg viewBox="0 0 16 16"><circle cx="8" cy="4.5" r="3.5"/><path d="M1.5 16c0-4 2.8-6.5 6.5-6.5s6.5 2.5 6.5 6.5z"/></svg>
    <span>Your Profile</span><span>|</span>
    <svg viewBox="0 0 16 16"><path d="M2 2h6v2H4v8h4v2H2z"/><path d="M8 5v2H5v2h3v2l5-3z"/></svg>
    <span>Log Out</span>
  </nav>
</header>

<section class="auth-band">
  <div class="auth-card">
    <h1 class="section-title">Login/Registration</h1>
    <div class="divider"></div>
    <div class="form-grid">
      <div class="field">First Name</div><div class="field">Last Name</div>
      <div class="field">Email Address</div><div class="field">Comfirm Email Address</div>
      <div class="field">Password</div><div class="field">Confirm Password</div>
    </div>
    <div class="submit">Submit</div>
    <div class="login-link">Log In</div>
  </div>
</section>

<section class="rankings">
  <h2 class="section-title">Top 3 Rankings</h2>
  <div class="divider"></div>

  <div class="rank-card" style="left:75px">
    <div class="avatar" role="img" aria-label="Portrait photo of ranked employee"></div>
    <div class="rank-body">
      <div class="rank-no">#1 Best</div>
      <div class="rank-name">Dan Harlow</div>
      <div class="rank-points">Points: 41</div>
      <div class="rank-reviews">Number of Reviews: <span>5 Views Details</span></div>
      <div class="trait">Smart:<div class="stars"><svg><use href="#star-full"/></svg><svg><use href="#star-full"/></svg><svg><use href="#star-full"/></svg><svg><use href="#star-empty"/></svg><svg><use href="#star-empty"/></svg></div></div>
      <div class="trait">Easy to work with:<div class="stars"><svg><use href="#star-full"/></svg><svg><use href="#star-full"/></svg><svg><use href="#star-full"/></svg><svg><use href="#star-empty"/></svg><svg><use href="#star-empty"/></svg></div></div>
      <div class="trait">Hard Worker:<div class="stars"><svg><use href="#star-full"/></svg><svg><use href="#star-full"/></svg><svg><use href="#star-full"/></svg><svg><use href="#star-empty"/></svg><svg><use href="#star-empty"/></svg></div></div>
    </div>
  </div>

  <div class="rank-card" style="left:435px">
    <div class="avatar" role="img" aria-label="Portrait photo of ranked employee"></div>
    <div class="rank-body">
      <div class="rank-no">#2 Best</div>
      <div class="rank-name">Dan Harlow</div>
      <div class="rank-points">Points: 4</div>
      <div class="rank-reviews">Number of Reviews: <span>5 Views Details</span></div>
      <div class="trait">Smart:<div class="stars"><svg><use href="#star-full"/></svg><svg><use href="#star-full"/></svg><svg><use href="#star-full"/></svg><svg><use href="#star-empty"/></svg><svg><use href="#star-empty"/></svg></div></div>
      <div class="trait">Easy to work with:<div class="stars"><svg><use href="#star-full"/></svg><svg><use href="#star-full"/></svg><svg><use href="#star-full"/></svg><svg><use href="#star-empty"/></svg><svg><use href="#star-empty"/></svg></div></div>
      <div class="trait">Hard Worker:<div class="stars"><svg><use href="#star-full"/></svg><svg><use href="#star-full"/></svg><svg><use href="#star-full"/></svg><svg><use href="#star-empty"/></svg><svg><use href="#star-empty"/></svg></div></div>
    </div>
  </div>

  <div class="rank-card" style="left:796px">
    <div class="avatar dark" role="img" aria-label="Portrait photo of ranked employee"></div>
    <div class="rank-body">
      <div class="rank-no">#3 Best</div>
      <div class="rank-name">Dan Harlow</div>
      <div class="rank-points">Points: 36</div>
      <div class="rank-reviews">Number of Reviews: <span>5 Views Details</span></div>
      <div class="trait">Smart:<div class="stars"><svg><use href="#star-full"/></svg><svg><use href="#star-full"/></svg><svg><use href="#star-full"/></svg><svg><use href="#star-empty"/></svg><svg><use href="#star-empty"/></svg></div></div>
      <div class="trait">Easy to work with:<div class="stars"><svg><use href="#star-full"/></svg><svg><use href="#star-full"/></svg><svg><use href="#star-full"/></svg><svg><use href="#star-empty"/></svg><svg><use href="#star-empty"/></svg></div></div>
      <div class="trait">Hard Worker:<div class="stars"><svg><use href="#star-full"/></svg><svg><use href="#star-full"/></svg><svg><use href="#star-full"/></svg><svg><use href="#star-empty"/></svg><svg><use href="#star-empty"/></svg></div></div>
    </div>
  </div>
</section>

<footer class="site-footer">Copyright © 2016. All Right Reserved</footer>
</body>
</html>
```